The name of the company is Harbor Turns buying foreclosed homes and remodeling

A sleek classy card. It’s a home remodel and house flip company. Something mostly black with dark gray and red in color . Something with two f”s as a logo on front as shown in pictures. Kind of just let you guys run with it . I left a few pictures that should help
You guys get an idea of what I thought was good also left all the information for back of the card

Target Market(s)

Home remodel consumers

Industry/Entity Type

Construction Company

Contact Information for Business Card

All details are on photo

Font styles to use
Decorative

Colors

Designer to choose colors to be used in the design.

Requirements
Must have
• Name of company on front. Harbor Turns
Nice to have
• Up to you guys I trust you
Should not have
• Not sure

```html
<!DOCTYPE html>
<html lang="en">
<head>
<meta charset="utf-8">
<title>Harbor Turns — Business Card</title>
<link rel="stylesheet" href="https://fonts.googleapis.com/css2?family=Montserrat:wght@400;500;700;800&display=swap">
<style>
  :root {
    --stage: #2b2826;
    --card: #050505;
    --card-edge: #1a1a1a;
    --mark-gray: #2e2e2e;
    --deco-gray: #1a1a1a;
    --text-light: #d9d9d9;
    --accent-red: #e0121b;
  }
  * { box-sizing: border-box; margin: 0; padding: 0; }
  html, body { width: 1200px; height: 1000px; overflow: hidden; }
  body {
    background: var(--stage);
    font-family: "Montserrat", Arial, sans-serif;
    position: relative;
  }
  .card {
    position: absolute;
    width: 540px;
    height: 309px;
    background: linear-gradient(135deg, #0c0c0c 0%, var(--card) 60%);
    border: 1px solid var(--card-edge);
    box-shadow: 0 18px 40px rgba(0,0,0,.55);
    overflow: hidden;
  }
  .card--contact { left: 40px; top: 345px; }
  .card--brand { left: 620px; top: 345px; }

  .brand-name {
    font-weight: 800;
    color: var(--mark-gray);
    text-transform: uppercase;
    letter-spacing: 1px;
    display: flex;
    align-items: center;
    gap: 10px;
    white-space: nowrap;
  }
  .brand-name .square {
    width: 14px; height: 14px; background: var(--mark-gray); display: inline-block;
  }
  .card--contact .brand-name { position: absolute; left: 40px; top: 38px; font-size: 26px; }

  .deco-name {
    position: absolute;
    font-weight: 800;
    color: var(--deco-gray);
    text-transform: uppercase;
    line-height: .95;
    font-size: 52px;
    white-space: nowrap;
    pointer-events: none;
  }
  .card--contact .deco-name { right: 26px; bottom: 30px; text-align: right; }
  .card--brand .deco-name { left: 28px; top: 28px; }

  .holder {
    position: absolute; left: 40px; top: 118px;
    color: var(--accent-red); font-size: 17px; font-weight: 500;
    white-space: nowrap;
  }
  .contacts { position: absolute; left: 40px; top: 152px; list-style: none; }
  .contacts li {
    display: flex; align-items: center; gap: 8px;
    color: var(--text-light); font-size: 11.5px; margin-bottom: 6px;
    white-space: nowrap;
  }
  .contacts svg { width: 11px; height: 11px; flex: none; }
  .contacts .hl { color: var(--accent-red); }

  .card--brand .brand-name { position: absolute; right: 40px; top: 150px; font-size: 24px; }
  .services { position: absolute; right: 40px; top: 200px; list-style: none; }
  .services li {
    display: flex; align-items: center; gap: 8px;
    color: var(--text-light); font-size: 13px; font-weight: 500;
    text-transform: uppercase; letter-spacing: .5px; margin-bottom: 6px;
    white-space: nowrap;
  }
  .services li::before {
    content: ""; width: 7px; height: 7px; background: var(--accent-red);
  }
</style>
</head>
<body>

<section class="card card--contact">
  <div class="deco-name" aria-hidden="true">Harbor<br>Turns</div>
  <div class="brand-name"><span class="square"></span>Harbor Turns</div>
  <p class="holder">Daniel Whitcombe JR.</p>
  <ul class="contacts">
    <li>
      <svg viewBox="0 0 12 12"><circle cx="6" cy="6" r="6" fill="#e0121b"/><path d="M4 3.2l1 1.3-.6.7a4 4 0 0 0 2.4 2.4l.7-.6 1.3 1-.7 1A5.5 5.5 0 0 1 3 4z" fill="#050505"/></svg>
      <span>555-014-2286</span>
    </li>
    <li>
      <svg viewBox="0 0 12 12"><circle cx="6" cy="6" r="6" fill="#e0121b"/><rect x="3" y="4" width="6" height="4.2" fill="none" stroke="#050505" stroke-width="1"/><path d="M3 4l3 2.3L9 4" fill="none" stroke="#050505" stroke-width="1"/></svg>
      <span>whitcombejr@com</span>
    </li>
    <li>
      <svg viewBox="0 0 12 12"><circle cx="6" cy="6" r="6" fill="#e0121b"/><circle cx="6" cy="6" r="3" fill="none" stroke="#050505" stroke-width="1"/><path d="M3 6h6M6 3v6" stroke="#050505" stroke-width=".8"/></svg>
      <span>www.<span class="hl">harborturns</span>.com</span>
    </li>
    <li>
      <svg viewBox="0 0 12 12"><circle cx="6" cy="6" r="6" fill="#e0121b"/><rect x="3.3" y="3.3" width="5.4" height="5.4" rx="1.5" fill="none" stroke="#050505" stroke-width="1"/></svg>
      <span>harbor_turns</span>
    </li>
  </ul>
</section>

<section class="card card--brand">
  <div class="deco-name" aria-hidden="true">Harbor<br>Turns</div>
  <div class="brand-name"><span class="square"></span>Harbor Turns</div>
  <ul class="services">
    <li>General Gontractor</li>
    <li>Home Remodel</li>
    <li>Concrete Altenitius</li>
  </ul>
</section>

</body>
</html>
```